KRV

I just wrote a novel that I plan on marketing through my website. Please use my uploaded files to add on to your design... The name of the book is "Ashes beneath the orchard".

Industry/Entity Type

Marketing

Font styles to use
Serif
Sans Serif

Colors

Designer to choose colors to be used in the design.

```html
<!DOCTYPE html>
<html lang="en">
<head>
<meta charset="utf-8">
<title>Ashes Beneath the Orchard</title>
<link rel="stylesheet" href="https://fonts.googleapis.com/css2?family=Ubuntu:wght@400;500;700&family=Arimo:wght@400&display=swap">
<style>
:root{
  --ink:#1b1b1b;
  --text:#333333;
  --muted:#666666;
  --red:#d4202a;
  --red-dark:#a8151d;
  --navy:#2c2870;
  --paper:#f4f0ec;
  --line:#dcd8d4;
  --white:#ffffff;
}
*{box-sizing:border-box;margin:0;padding:0}
html,body{width:1200px;height:960px;overflow:hidden}
body{position:relative;background:var(--white);font-family:'Ubuntu',sans-serif;color:var(--text)}
.abs{position:absolute}

.site-header{position:absolute;left:0;top:0;width:1200px;height:148px;background:var(--white);border-bottom:1px solid var(--line)}
.brand{left:110px;top:10px;display:flex;align-items:center;gap:14px}
.brand-mark{width:124px;height:124px;border-radius:50%;background:var(--ink);display:flex;align-items:center;justify-content:center;color:var(--white);font-weight:700;font-size:34px}
.social{display:flex;gap:6px}
.social span{width:35px;height:35px;border-radius:50%;background:var(--navy);display:block}
.header-social{right:111px;top:26px}
.contact-line{right:111px;top:80px;font-size:16px;font-weight:500;color:#444}
.contact-line b{color:var(--red);font-weight:500}
.main-nav{right:110px;top:115px;display:flex;font-size:15px;color:#444}
.main-nav a{color:inherit;text-decoration:none;padding:0 9px;border-left:1px solid #ccc;line-height:14px}
.main-nav a:first-child{border-left:none}
.main-nav a:last-child{padding-right:0}

.hero-band{position:absolute;left:0;top:148px;width:1200px;height:735px;background:var(--paper);
  background-image:radial-gradient(rgba(0,0,0,.035) 1px,transparent 1px);background-size:4px 4px}
.slide-arrow{width:38px;height:38px;border:3px solid #2b2b2b;border-radius:50%;display:flex;align-items:center;justify-content:center}
.arrow-prev{left:109px;top:346px}
.arrow-next{left:1053px;top:346px}
.hero-title{left:182px;top:226px;font-size:24px;font-weight:700;color:var(--ink);line-height:34px}
.hero-copy{left:182px;top:298px;width:320px;font-family:'Arimo',sans-serif;font-size:12px;line-height:23px;color:#333}
.buy-btn{left:183px;top:403px;width:120px;height:46px;border-radius:4px;background:linear-gradient(#e52a33,var(--red-dark));color:var(--white);font-size:20px;font-weight:500;display:flex;align-items:center;justify-content:center;box-shadow:3px 3px 0 #fff,3px 4px 4px rgba(0,0,0,.25)}
.book-back{left:535px;top:292px;width:225px;height:210px;transform:rotate(-19deg);background:linear-gradient(135deg,#3a3590,#272266 60%,#1f1b55);border:4px solid var(--white);box-shadow:0 3px 8px rgba(0,0,0,.3)}
.poster{left:764px;top:169px;width:278px;height:357px;background:var(--white);padding:5px;box-shadow:0 2px 6px rgba(0,0,0,.25)}
.poster-art{width:100%;height:100%;background:linear-gradient(180deg,#e8e4e6 0%,#b9a9ad 35%,#6d4f58 65%,#1e1a24 100%)}

.card{position:absolute;top:550px;width:304px;height:307px;background:var(--white);border:1px solid var(--line);border-radius:4px;box-shadow:0 1px 3px rgba(0,0,0,.08)}
.card h2{position:absolute;left:24px;top:20px;font-size:21px;font-weight:500;color:var(--ink)}
.card-icon{position:absolute;right:16px;top:13px}
.card p{font-size:13.5px;line-height:20px;color:#333}
.about{left:110px}
.about .body{position:absolute;left:24px;top:52px;width:270px}
.about .body p+p{margin-top:10px}
.blog{left:447px}
.blog .body{position:absolute;left:24px;top:52px;width:270px}
.post-time{font-size:11px;color:var(--muted);margin:4px 0 10px}
.more-btn{position:absolute;left:25px;top:260px;width:108px;height:28px;background:var(--navy);color:var(--white);font-size:14px;border-radius:2px;display:flex;align-items:center;justify-content:center}
.ask{left:784px}
.field{position:absolute;left:27px;width:265px;height:30px;border:1px solid #d8d8d8;border-radius:3px;background:linear-gradient(#fff,#f4f4f4);font-size:12px;color:#444;padding:7px 12px}
.field.area{height:73px}
.go-btn{position:absolute;right:20px;top:20px;width:40px;height:40px;border-radius:50%;background:var(--navy);color:var(--white);font-weight:500;font-size:15px;display:flex;align-items:center;justify-content:center}
.caret{position:absolute;right:10px;top:11px;width:0;height:0;border-left:5px solid transparent;border-right:5px solid transparent;border-top:8px solid #666}

.site-footer{position:absolute;left:0;top:883px;width:1200px;height:77px;background:var(--white);border-top:1px solid var(--line)}
.foot-nav{left:110px;top:20px;display:flex;gap:17px;font-size:13px;color:#777}
.copyright{left:110px;top:43px;font-size:12px;color:#555}
.footer-social{right:111px;top:23px}
</style>
</head>
<body>

<header class="site-header">
  <div class="abs brand"><div class="brand-mark">KRV</div></div>
  <div class="abs social header-social"><span></span><span></span><span></span></div>
  <div class="abs contact-line">CONTACT MARA QUILL : <b>555-014-2291</b></div>
  <nav class="abs main-nav"><a>Home</a><a>About Us</a><a>News</a><a>Events</a><a>Contact Us</a></nav>
</header>

<section class="hero-band">
</section>

<div class="abs slide-arrow arrow-prev"><svg width="14" height="18" viewBox="0 0 14 18"><path d="M10 2 3 9l7 7" fill="none" stroke="#2b2b2b" stroke-width="3"/></svg></div>
<div class="abs slide-arrow arrow-next"><svg width="14" height="18" viewBox="0 0 14 18"><path d="M4 2l7 7-7 7" fill="none" stroke="#2b2b2b" stroke-width="3"/></svg></div>

<h1 class="abs hero-title">ASHES BENEATH THE<br>ORCHARD</h1>
<div class="abs hero-copy">Lorem Ipsum is simply dummy text of the printing and typesetting industry. Lorem Ipsum has been the industry's standard dummy<br>text ever since the 1500s,</div>
<div class="abs buy-btn">Buy Now</div>

<div class="abs book-back" role="img" aria-label="Paperback book lying at an angle, navy cover with red title band and a cover photograph"></div>
<div class="abs poster"><div class="poster-art" role="img" aria-label="Book promotion poster with red title lettering, story photographs, price badge and ordering details"></div></div>

<article class="card about">
  <h2>About Ashes</h2>
  <svg class="card-icon" width="22" height="30" viewBox="0 0 22 30"><path d="M4 9a7 7 0 1 1 10 6c-2 1-3 2-3 5" fill="none" stroke="var(--red)" stroke-width="4.5"/><circle cx="11" cy="26.5" r="2.8" fill="var(--red)"/></svg>
  <div class="body">
    <p>Lorem Ipsum is simply dummy text of the printing and typesetting industry. Lorem Ipsum has been the industry's standard dummy text ever since the 1500s, when an unknown printer took a galley of type and scrambled it to make a type specimen book.</p>
    <p>It has survived not only five centuries, but also the leap into electronic typesetting, remaining essentially unchanged.</p>
  </div>
  <div class="more-btn">Learn More</div>
</article>

<article class="card blog">
  <h2>Our Blog</h2>
  <svg class="card-icon" width="28" height="28" viewBox="0 0 28 28"><path d="M3 3h22v15H12l-6 6v-6H3z" fill="none" stroke="var(--red)" stroke-width="3" stroke-linejoin="round"/><path d="M8 8v6" stroke="var(--red)" stroke-width="3"/></svg>
  <div class="body">
    <p>Lorem Ipsum is simply dummy text of the printing and typesetting industry</p>
    <div class="post-time">06:44:45 AM November 19th</div>
    <p>Lorem Ipsum is simply dummy text of the printing and typesetting industry</p>
    <div class="post-time">06:44:45 AM November 19th</div>
    <p>Lorem Ipsum is simply dummy text of the printing and typesetting industry</p>
    <div class="post-time">06:44:45 AM November 19th</div>
  </div>
  <div class="more-btn">Learn More</div>
</article>

<article class="card ask">
  <h2>Ask a Question</h2>
  <svg class="card-icon" width="28" height="26" viewBox="0 0 28 26"><path d="M2 11 14 2l12 9v13H2z" fill="var(--red)"/><path d="M6 12l8 6 8-6" fill="none" stroke="#fff" stroke-width="2"/></svg>
  <div class="field" style="top:55px">Name</div>
  <div class="field" style="top:96px">Phone Number</div>
  <div class="field" style="top:138px">Email Address</div>
  <div class="field" style="top:180px">Service<span class="caret"></span></div>
  <div class="field area" style="top:222px">Question<div class="go-btn">GO</div></div>
</article>

<footer class="site-footer">
  <nav class="abs foot-nav"><span>Home</span><span>About Us</span><span>News</span><span>Events</span><span>Contact Us</span></nav>
  <div class="abs copyright">Copyright © 2014 Ashes Beneath the Orchard. All Rights Reserved</div>
  <div class="abs social footer-social"><span></span><span></span><span></span></div>
</footer>

</body>
</html>
```